Pelican Litigation Funding Letterhead & Document Template

We need a letter head designed for our fund. Our fund works with law firms and investors across the globe. We need a a cover letter template as well as a document template for subsequent pages. Blue and white color scheme is preferred. This is our predecessor's website: https://www.pelicanvq.com/index.html. Please see our logo attached. The logo color code is #19478d. Font is Gotham-Medium.
Target Market(s)
Sophisticated investors and law firms
Font styles to use
Sans Serif
Colors
0255a3

```html
<!DOCTYPE html>
<html lang="en">
<head>
<meta charset="utf-8">
<title>Pelican Litigation Funding Letterhead</title>
<link href="https://fonts.googleapis.com/css2?family=Open+Sans:wght@400;600&family=Arimo:wght@700&display=swap" rel="stylesheet">
<style>
  :root {
    --brand-blue: #19478d;
    --band-blue: #0b418a;
    --page-bg: #e6e6e6;
    --paper: #fafafa;
    --body-text: #555555;
    --salutation: #505050;
    --band-shadow: #b9b9b9;
    --signature-tone: #d8dbe1;
  }
  * { margin: 0; padding: 0; box-sizing: border-box; }
  html, body { width: 1059px; height: 1200px; overflow: hidden; }
  body { background: var(--page-bg); position: relative; font-family: "Open Sans", sans-serif; }

  .letter {
    position: absolute; left: 121px; top: 24px;
    width: 816px; height: 1152px;
    background: var(--paper);
    overflow: hidden;
  }

  .letter-head {
    position: absolute; left: 0; top: 70px; width: 100%;
    display: flex; justify-content: center; align-items: center; gap: 10px;
  }
  .brand-square { width: 14px; height: 14px; background: var(--brand-blue); }
  .brand-name {
    font-family: "Open Sans", sans-serif; font-weight: 600;
    font-size: 19px; letter-spacing: 0.5px; color: var(--brand-blue);
    text-transform: uppercase;
  }

  .salutation {
    position: absolute; left: 69px; top: 214px;
    font-family: "Arimo", sans-serif; font-weight: 700;
    font-size: 18px; color: var(--salutation);
  }

  .letter-body {
    position: absolute; left: 70px; top: 262px; width: 683px;
    font-size: 15.6px; line-height: 21.3px; color: var(--body-text);
    text-align: justify; letter-spacing: -0.1px;
  }
  .letter-body p + p { margin-top: 21.3px; }

  .signature {
    position: absolute; left: 68px; top: 762px;
    width: 152px; height: 76px;
    background: var(--signature-tone); border-radius: 4px;
  }

  .letter-foot { position: absolute; left: 0; bottom: 0; width: 100%; height: 70px; }
  .letter-foot svg { position: absolute; left: 0; top: 0; }
  .foot-contacts {
    position: absolute; left: 0; width: 100%; top: 26px;
    display: flex; justify-content: center; gap: 8px;
    font-size: 13px; color: #ffffff;
  }
  .foot-contacts span { display: inline-flex; align-items: center; gap: 4px; }
  .foot-contacts svg { position: static; }
  .foot-address {
    position: absolute; left: 0; width: 100%; top: 45px;
    text-align: center; font-size: 11px; color: #ffffff;
  }
</style>
</head>
<body>
<main class="letter">
  <header class="letter-head">
    <span class="brand-square"></span>
    <span class="brand-name">Pelican Litigation Funding</span>
  </header>

  <h1 class="salutation">Dear Mr. John,</h1>

  <section class="letter-body">
    <p>Lorem Ipsum is simply dummy text of the printing and typesetting industry. Lorem Ipsum has been the industry's standard dummy text ever since the 1500s, when an unknown printer took a galley of type and scrambled it to make a type specimen book. It has survived not only five centuries, but also the leap into electronic typesetting, remaining essentially unchanged.</p>
    <p>The standard chunk of Lorem Ipsum used since the 1500s is reproduced below for those interested. Sections 1.10.32 and 1.10.33 from "de Finibus Bonorum et Malorum" by Cicero are also reproduced in their exact original form, accompanied by English versions from the 1914 translation by H. Rackham</p>
    <p>Lorem Ipsum is simply dummy text of the printing and typesetting industry. Lorem Ipsum has been the industry's standard dummy text ever since the 1500s, when an unknown printer took a galley of type and scrambled it to make a type specimen book. It has survived not only five centuries, but also the leap into electronic typesetting, remaining essentially unchanged. It was popularised in the</p>
    <p>The standard chunk of Lorem Ipsum used since the 1500s is reproduced below for those interested. Sections 1.10.32 and 1.10.33 from "de Finibus Bonorum et Malorum" by Cicero are also reproduced in their exact original form, accompanied by English versions from the 1914 translation by H. Rackham</p>
  </section>

  <div class="signature" role="img" aria-label="Handwritten signature of the sender"></div>

  <footer class="letter-foot">
    <svg width="816" height="70" viewBox="0 0 816 70" aria-hidden="true">
      <path d="M95 0 L95 10 Q400 22 816 10 L816 14 L95 14 Z" fill="var(--band-shadow)"/>
      <path d="M0 4 Q420 30 816 8 L816 70 L0 70 Z" fill="var(--band-blue)"/>
    </svg>
    <div class="foot-contacts">
      <span><svg width="10" height="10" viewBox="0 0 10 10" aria-hidden="true"><path d="M2 0 L4 2.5 L3 4 Q4.5 6 6 7 L7.5 6 L10 8 L8.5 10 Q2 9 0 1.5 Z" fill="#fff"/></svg>(555) 014-7200</span>
      <span><svg width="11" height="10" viewBox="0 0 11 10" aria-hidden="true"><rect x="3" y="0" width="5" height="3" fill="#fff"/><rect x="0" y="4" width="11" height="6" rx="1" fill="#fff"/></svg>(555) 014-7300</span>
      <span><svg width="10" height="8" viewBox="0 0 10 8" aria-hidden="true"><rect width="10" height="8" fill="#fff"/><path d="M0 0 L5 4.5 L10 0" stroke="var(--band-blue)" fill="none"/></svg>info@pelicanvq.com</span>
      <span><svg width="10" height="10" viewBox="0 0 10 10" aria-hidden="true"><circle cx="5" cy="5" r="5" fill="#fff"/><path d="M0 5 H10 M5 0 V10" stroke="var(--band-blue)" stroke-width="0.8"/></svg>www.pelicanvq.com</span>
    </div>
    <div class="foot-address">Harbor Point - Penthouse Floor 4100 Meridian Avenue, Suite 1750 Houston, Texas 77001</div>
  </footer>
</main>
</body>
</html>
```